Vendra Corporate Letterhead

- We would like a letterhead using our logo (can be supplied as vector if needed)
- Would like to have the logo on a clear background
- Please send logo design as a separate file
- Letterhead information:
Vendra Power Inc.
482 S. Maple Ave. Suite 214
Pasadena, CA 91123

Colors
0555a3
3276b5
85abd2
000000
1b1b1b
757575
c7c7c7
e8e8e8

```html
<!DOCTYPE html>
<html lang="en">
<head>
<meta charset="utf-8">
<title>Vendra Corporate Letterhead</title>
<link rel="stylesheet" href="https://fonts.googleapis.com/css2?family=Arimo:wght@400;700&family=PT+Sans:wght@400&family=Dancing+Script:wght@400&display=swap">
<style>
  :root {
    --brand-blue: #0555a3;
    --brand-mid: #3276b5;
    --brand-light: #85abd2;
    --ink-black: #000000;
    --ink-dark: #1b1b1b;
    --ink-grey: #757575;
    --line-grey: #c7c7c7;
    --backdrop: #e8e8e8;
    --paper: #ffffff;
    --band-navy: #0b4a78;
  }
  * { margin: 0; padding: 0; box-sizing: border-box; }
  html, body { width: 1112px; height: 1200px; overflow: hidden; background: var(--backdrop); }
  .canvas { position: relative; width: 1112px; height: 1200px; }
  .sheet {
    position: absolute; left: 210px; top: 80px; width: 708px; height: 1000px;
    background: var(--paper); overflow: hidden;
    font-family: "Arimo", Arial, sans-serif; color: var(--ink-dark);
  }
  .brand {
    position: absolute; left: 66px; top: 72px;
    display: flex; align-items: center; gap: 10px;
    font-family: "Arimo", Arial, sans-serif; font-weight: 700;
    font-size: 56px; line-height: 1; color: var(--brand-blue);
  }
  .brand-dot { width: 16px; height: 16px; border-radius: 50%; background: var(--brand-blue); }
  .letter-date { position: absolute; left: 62px; top: 239px; font-size: 16px; color: #333; }
  .recipient { position: absolute; left: 62px; top: 276px; font-size: 16px; line-height: 18.6px; color: #333; }
  .salutation { position: absolute; left: 61px; top: 398px; font-size: 16px; font-weight: 700; color: #444; }
  .letter-body {
    position: absolute; left: 62px; top: 437px; width: 583px;
    font-size: 14.6px; line-height: 17.3px; color: var(--ink-grey);
    text-align: justify;
  }
  .letter-body p { margin-bottom: 17.3px; }
  .closing {
    position: absolute; right: 63px; top: 765px; text-align: right;
    font-size: 14.6px; line-height: 17.3px; color: var(--ink-dark);
  }
  .signature {
    font-family: "Dancing Script", cursive; font-size: 30px; line-height: 40px;
    color: var(--brand-blue); margin: 2px 0 6px;
  }
  .footer-band { position: absolute; left: 0; bottom: 0; width: 708px; height: 88px; }
  .footer-address {
    position: absolute; left: 60px; bottom: 21px;
    font-family: "PT Sans", sans-serif; font-size: 16px; color: var(--paper);
  }
  .footer-contacts {
    position: absolute; left: 542px; top: 929px; list-style: none;
    font-family: "PT Sans", sans-serif; font-size: 13.5px; line-height: 17.4px; color: var(--paper);
  }
  .footer-contacts li { display: flex; align-items: center; gap: 6px; }
  .footer-contacts svg { width: 13px; height: 12px; fill: var(--paper); }
</style>
</head>
<body>
<div class="canvas">
  <div class="sheet">
    <div class="brand"><span class="brand-dot"></span><span>Vendra</span></div>

    <div class="letter-date">January 12, 2014</div>
    <div class="recipient">
      Mr. John Doe<br>President<br>AA Corporation<br>111 Street Name, Suite#<br>City, State, 12345
    </div>
    <div class="salutation">Dear Mr. John,</div>

    <div class="letter-body">
      <p>Lorem Ipsum is simply dummy text of the printing and typesetting industry. Lorem Ipsum has been the industry's standard dummy text ever since the 1500s, when an unknown printer took a galley of type and scrambled it to make a type specimen book. It has survived not only five centuries, but also the leap into electronic typesetting, remaining essentially unchanged.</p>
      <p>The standard chunk of Lorem Ipsum used since the 1500s is reproduced below for those interested. Sections 1.10.32 and 1.10.33 from "de Finibus Bonorum et Malorum" by Marcus Venn are also reproduced in their exact original form, accompanied by English versions from the 1914 translation by H. Ramsay</p>
      <p>Lorem Ipsum is simply dummy text of the printing and typesetting industry. Lorem Ipsum has been the industry's standard dummy text ever since the 1500s, when an unknown printer took a galley of type and scrambled it to make a type specimen book. It has survived not only five centuries, but also the leap into electronic typesetting, remaining essentially unchanged. It was popularised in the</p>
    </div>

    <div class="closing">
      Sincerely Your,
      <div class="signature">your name</div>
      Name Last Name<br>Company Name
    </div>

    <svg class="footer-band" viewBox="0 0 708 88" aria-hidden="true">
      <defs>
        <linearGradient id="band-grey" x1="0" x2="1" y1="0" y2="0">
          <stop offset="0" stop-color="#6e6e6e"/>
          <stop offset="0.55" stop-color="#4a4a4a"/>
          <stop offset="0.85" stop-color="#1f2a35"/>
        </linearGradient>
        <linearGradient id="band-blue" x1="0" x2="1" y1="0" y2="0">
          <stop offset="0" stop-color="#1d3347"/>
          <stop offset="0.35" stop-color="#0b4470"/>
          <stop offset="1" stop-color="#0b4a78"/>
        </linearGradient>
      </defs>
      <rect x="0" y="40" width="708" height="48" fill="url(#band-grey)"/>
      <path d="M350 40 C440 40 455 38 478 22 C500 6 515 0 548 0 L708 0 L708 88 L350 88 Z" fill="url(#band-blue)"/>
      <path d="M0 40 L370 40 C380 40 385 42 392 46" stroke="#8a8a8a" stroke-width="1" fill="none" opacity="0.5"/>
    </svg>

    <div class="footer-address">482 S. Maple Ave. Suite 214, Pasadena, CA 91123</div>

    <ul class="footer-contacts">
      <li><svg viewBox="0 0 13 12"><path d="M1 4 C1 2 3 1 6.5 1 C10 1 12 2 12 4 L10 5 L9 3.5 L4 3.5 L3 5 Z M3 6 L10 6 L11 11 L2 11 Z"/></svg>626-555-0142</li>
      <li><svg viewBox="0 0 13 12"><path d="M1 2 H12 V10 H1 Z M1.8 2.8 L6.5 6.6 L11.2 2.8 V9.2 L8 6.4 L6.5 7.6 L5 6.4 L1.8 9.2 Z" fill-rule="evenodd"/></svg>info@vendrapower.com</li>
      <li><svg viewBox="0 0 13 12"><circle cx="6.5" cy="6" r="5.2" fill="none" stroke="#fff" stroke-width="1.2"/><path d="M1.3 6 H11.7 M6.5 0.8 V11.2" stroke="#fff" stroke-width="1"/><ellipse cx="6.5" cy="6" rx="2.4" ry="5.2" fill="none" stroke="#fff" stroke-width="1"/></svg>www.vendrapower.com</li>
    </ul>
  </div>
</div>
</body>
</html>
```